Hi,

I would like to have a invitation made for a party. exactly like the picture in the link below.

http://pinboardia.example/pin/730215948361027459/

However, Please change the colors into fun/ girly feeling. font can be different and size of the card should be the same

Name of the girl: RINA
What: Bachelorette Party
Where:TOLO Boat
Dubai Coral Quay Sailing Club
When:7th of February 2013

No RSVP required. (so no need to put it)

```html
<!DOCTYPE html>
<html lang="en">
<head>
<meta charset="utf-8">
<title>Rina's Bachelorette Invitation</title>
<link rel="stylesheet" href="https://fonts.googleapis.com/css2?family=Alfa+Slab+One&family=Rye&family=Pinyon+Script&family=EB+Garamond:wght@400&display=swap">
<style>
  :root {
    --page: #ffffff;
    --page-edge: #f4f2c8;
    --card: #e8d9c4;
    --ornament: #7a5c55;
    --bird: #8a7866;
    --script-brown: #6b5446;
    --mauve: #8c5672;
    --hot-pink: #f2137a;
    --magenta: #e010d8;
    --frame: #8a4f80;
    --frame-dots: #9a3fb0;
  }
  * { margin: 0; padding: 0; box-sizing: border-box; }
  html, body { width: 1200px; height: 1002px; overflow: hidden; background: var(--page); }
  .canvas {
    position: relative; width: 1200px; height: 1002px;
    border: 1px solid var(--page-edge); background: var(--page);
  }
  .invitation {
    position: absolute; left: 36px; top: 70px; width: 1164px; height: 508px;
    background: var(--card);
  }
  .ornament, .bird, .flourish { position: absolute; }
  .ornament { background: var(--ornament); opacity: .55; }
  .ornament--top { left: 288px; top: 22px; width: 68px; height: 62px; }
  .ornament--bottom { left: 14px; top: 435px; width: 62px; height: 62px; }
  .bird { left: 516px; top: 100px; width: 104px; height: 96px; background: var(--bird); opacity: .5; border-radius: 40% 60% 45% 55%; }
  .host-name {
    position: absolute; left: 54px; top: 108px;
    font-family: "Pinyon Script", cursive; font-size: 70px; line-height: 1;
    color: var(--script-brown);
  }
  .tagline {
    position: absolute; left: 12px; top: 216px; width: 726px;
    font-family: "Alfa Slab One", serif; font-size: 33px; line-height: 1;
    letter-spacing: 1.5px; color: var(--mauve); white-space: nowrap;
    text-align: justify; text-align-last: justify;
  }
  .headline {
    position: absolute; left: 10px; top: 258px; width: 742px;
    font-family: "Rye", serif; font-size: 132px; line-height: 1;
    color: var(--hot-pink); white-space: nowrap;
    text-align: justify; text-align-last: justify;
  }
  .details-frame { position: absolute; left: 790px; top: 60px; width: 290px; height: 400px; }
  .flourish { width: 32px; height: 26px; background: var(--frame); opacity: .7; border-radius: 50% 50% 40% 40%; top: 155px; }
  .flourish--left { left: 794px; }
  .flourish--right { left: 1046px; }
  .details {
    position: absolute; left: 806px; top: 138px; width: 260px;
    text-align: center; list-style: none;
  }
  .details dt {
    font-family: "Alfa Slab One", serif; font-size: 15px; line-height: 1;
    color: var(--magenta); margin-top: 14px;
  }
  .details dt:first-child { margin-top: 0; }
  .details dd {
    font-family: "EB Garamond", serif; font-size: 17px; line-height: 1.15;
    color: var(--mauve); margin-top: 4px;
  }
  .details dd.guest {
    font-family: "Pinyon Script", cursive; font-size: 30px; color: var(--hot-pink);
    margin-top: 0;
  }
  .details dd.venue { font-size: 13px; line-height: 1.35; }
</style>
</head>
<body>
<div class="canvas">
  <section class="invitation">
    <div class="ornament ornament--top" role="img" aria-label="Vintage filigree corner ornament"></div>
    <div class="bird" role="img" aria-label="Engraved illustration of a bird in flight"></div>
    <div class="ornament ornament--bottom" role="img" aria-label="Vintage filigree corner ornament"></div>

    <h1 class="host-name">Rina's</h1>
    <p class="tagline">LAST CHANCE TO CELEBRATE BEING</p>
    <p class="headline">SINGLE</p>

    <svg class="details-frame" viewBox="0 0 290 400" aria-hidden="true">
      <g fill="var(--magenta)">
        <path d="M124 5 L130 18 L137 2 L145 18 L152 2 L159 18 L166 5 L164 28 H126 Z"/>
        <rect x="126" y="31" width="38" height="4"/>
      </g>
      <path d="M48 103 V58 Q48 42 70 42 H222 Q244 42 244 58 V103" fill="none"
            stroke="var(--frame)" stroke-width="3" stroke-dasharray="0 8" stroke-linecap="round"/>
      <path d="M52 396 V126 H58 V108 Q58 60 105 60 H190 Q238 60 238 108 V126 H258 V396"
            fill="none" stroke="var(--frame)" stroke-width="1.6"/>
      <path d="M60 390 V132 H66 V110 Q66 68 108 68 H188 Q230 68 230 110 V132 H252 V390"
            fill="none" stroke="var(--frame)" stroke-width="1"/>
      <path d="M264 126 V396" stroke="var(--frame-dots)" stroke-width="3" stroke-dasharray="0 8" stroke-linecap="round"/>
      <path d="M52 406 H264" stroke="var(--frame)" stroke-width="3" stroke-dasharray="0 8" stroke-linecap="round"/>
    </svg>
    <div class="flourish flourish--left" role="img" aria-label="Small scroll flourish"></div>
    <div class="flourish flourish--right" role="img" aria-label="Small scroll flourish"></div>

    <dl class="details">
      <dt>WHO</dt>
      <dd class="guest">Rina</dd>
      <dt>WHAT</dt>
      <dd>Bachelorette Party</dd>
      <dt>WHEN</dt>
      <dd>7th of February 2013</dd>
      <dt>WHERE</dt>
      <dd class="venue">TOLO Boat<br>Dubai Coral Quay Sailing Club</dd>
    </dl>
  </section>
</div>
</body>
</html>
```